Weight loss surgery restaurant card

We need to create a card for patients who have undergone weight loss surgery to take to restaurants so they can request smaller meals. These patients have had surgery on their stomach so that they can only consume half to one cup of food at a time. So normal sized restaurant meals are way too big (and cost a lot). This card they can present to the restaurant to communicate the fact that they have had weight loss surgery and therefore request a smaller meal portion at reduced cost

Target Market(s)

Restaurants serving weight loss surgery patients

Industry/Entity Type

Health Care

Contact Information for Business Card

This will be a plastic card similar to business card size.

Requirements
Must have
• The front of the card should include the following text:
• The individual bearing this card has undergone weight loss surgery.
• This surgery restricts portion sizes to between half and one cup of food at a time.
• Please give consideration to allowing smaller portions of your regular meals to be ordered to reduce wastage and excess costs.
• Example: a half size portion priced at two thirds of usual cost.
• The back of the card will have spaces for the person to write certain information. These are the categories that can be filled in by hand:
• Name:
• Procedure performed:
• Date of procedure (month/year):
• Treating Clinic Name:
• Treating Clinic Signature:
• Somewhere down the bottom should be something along the lines of:
• supplied from bernardwhitlow.com.au
Nice to have
• A nice design with imagery/colours etc ... not just the text on a white background! Bright attractive colours preferred.
• I have uploaded my logo ... a roughly triangular image followed by my name etc. The triangular logo image could be used somewhere on the card and this logo can be interchangeable for other clinics who purchase the card.
• **Please note that I don't want my name to be included as part of the logo on the card ... just use the triangular image on the side of the logo without the following name**
• Also, the colouring of the card does not have to reflect my logo colours as I am anticipating interchanging this logo with other logos if other clinics choose to adopt the card. I am interested to see other, more generic, colour choices as well as my logo colours

```html
<!DOCTYPE html>
<html lang="en">
<head>
<meta charset="utf-8">
<title>Weight Loss Surgery Restaurant Card</title>
<link rel="stylesheet" href="https://fonts.googleapis.com/css2?family=Roboto+Condensed:wght@300;400;700&family=Ubuntu:wght@500;700&display=swap">
<style>
  :root {
    --stage: #138278;
    --teal: #168a7c;
    --teal-soft: #5fb3a0;
    --grey: #7b7d80;
    --ink-light: #6f7174;
    --back-blue: #bfdce0;
    --row-line: #b7d6da;
  }
  * { box-sizing: border-box; margin: 0; padding: 0; }
  html, body { width: 1014px; height: 1200px; overflow: hidden; }
  body {
    background: var(--stage);
    font-family: "Roboto Condensed", "Arial Narrow", sans-serif;
    position: relative;
  }
  .card {
    position: absolute;
    left: 97px;
    width: 844px;
    overflow: hidden;
    box-shadow: 4px 6px 10px rgba(0,0,0,0.35);
  }
  .card--front {
    top: 87px;
    height: 481px;
    background: linear-gradient(160deg, #ffffff 0%, #f4f4f4 40%, #ffffff 60%, #ececec 100%);
  }
  .card--front::before {
    content: "";
    position: absolute; left: 0; right: 0; top: 0; height: 40px;
    background: linear-gradient(90deg, #f2f2f2, #d6d3d0);
    opacity: .6;
  }
  .card--front .bottom-band {
    position: absolute; left: 0; right: 0; bottom: 0; height: 38px;
    background: linear-gradient(180deg, #ffffff 0%, #c9d6d3 55%, #8fa6a1 100%);
  }
  .plate-art {
    position: absolute;
    border-radius: 50%;
    background: radial-gradient(circle, rgba(95,179,160,0.35) 0%, rgba(95,179,160,0.18) 55%, rgba(160,160,160,0.25) 72%, rgba(95,179,160,0.35) 100%);
  }
  .card--front .plate-art { left: 5px; top: 50px; width: 274px; height: 274px; }
  .headline {
    position: absolute; left: 331px; top: 54px;
    font-family: "Ubuntu", sans-serif; font-weight: 700;
    font-size: 41px; line-height: 42px; color: var(--teal);
    letter-spacing: -0.5px; white-space: nowrap;
  }
  .headline .accent { color: var(--grey); }
  .facts {
    position: absolute; left: 313px; top: 209px; width: 531px;
    list-style: none;
  }
  .facts li {
    position: relative; padding: 0 0 0 20px;
    font-size: 24px; line-height: 25px; color: var(--teal); font-weight: 400;
    white-space: nowrap;
  }
  .facts li + li { margin-top: 11px; }
  .facts li:nth-child(2) { background: rgba(255,255,255,0.7); }
  .facts li:nth-child(odd) { background: rgba(232,236,236,0.45); }
  .facts li::before {
    content: ""; position: absolute; left: 2px; top: 8px;
    width: 9px; height: 9px; border-radius: 50%; background: var(--teal);
  }
  .facts strong { font-weight: 700; }
  .example {
    position: absolute; left: 336px; top: 413px;
    font-size: 16px; color: var(--ink-light); white-space: nowrap;
  }
  .clinic-mark {
    position: absolute; display: flex; align-items: center; gap: 7px;
    white-space: nowrap;
  }
  .clinic-mark .dot {
    width: 34px; height: 34px; border-radius: 50%; background: var(--teal);
  }
  .clinic-mark .name {
    font-family: "Roboto Condensed", sans-serif; font-weight: 700;
    font-size: 22px; color: var(--teal); letter-spacing: 1px; text-transform: uppercase;
  }
  .card--front .clinic-mark { left: 30px; top: 400px; }

  .card--back {
    top: 617px;
    height: 482px;
    background: radial-gradient(ellipse at 60% 70%, #ffffff 0%, #e6f1f2 35%, var(--back-blue) 75%);
  }
  .card--back .plate-art { left: 587px; top: 75px; width: 258px; height: 258px; opacity: .8; }
  .fields { position: absolute; left: 0; right: 0; top: 117px; list-style: none; }
  .fields li {
    position: relative; height: 44px;
    padding-left: 79px; font-size: 29px; line-height: 42px; color: var(--teal);
    background: linear-gradient(90deg, rgba(255,255,255,0.85) 0%, rgba(255,255,255,0.9) 70%, rgba(255,255,255,0.2) 100%);
    border-bottom: 3px solid var(--row-line);
    white-space: nowrap;
  }
  .fields li::before {
    content: ""; position: absolute; left: 41px; top: 17px;
    width: 10px; height: 10px; border-radius: 50%; background: var(--teal-soft);
  }
  .fields .slash { position: absolute; left: 511px; }
  .supplied {
    position: absolute; left: 79px; top: 405px;
    font-size: 24px; letter-spacing: -0.4px; color: var(--teal); font-weight: 300;
    white-space: nowrap;
  }
  .supplied .site { color: var(--grey); }
  .card--back .clinic-mark { left: 566px; top: 406px; }
</style>
</head>
<body>
  <section class="card card--front">
    <div class="plate-art" role="img" aria-label="Dashed plate ring with fork and knife illustration"></div>
    <h1 class="headline">the individual bearing<br>this card has undergone<br><span class="accent">weight loss surgery</span></h1>
    <ul class="facts">
      <li>Around <strong>500,000</strong> of these procedures<br>are performed around the world every year.</li>
      <li>This surgery restricts portion sizes to<br>between <strong>half and one cup</strong> of food at a time.</li>
      <li>Please give consideration to allowing <strong>smaller</strong><br><strong>portions</strong> of your regular meals to be ordered<br>to <strong>reduce wastage</strong> and <strong>excess costs</strong>.</li>
    </ul>
    <p class="example">For example: a half size portion priced at two thirds of usual cost.</p>
    <div class="clinic-mark"><span class="dot"></span><span class="name">Bernard Whitlow</span></div>
    <div class="bottom-band"></div>
  </section>

  <section class="card card--back">
    <div class="plate-art" role="img" aria-label="Faint dashed plate ring with fork and knife illustration"></div>
    <ul class="fields">
      <li>Name:</li>
      <li>Procedure performed:</li>
      <li>Date of procedure (month/year):<span class="slash">/</span></li>
      <li>Treating Clinic Name:</li>
      <li>Treating Clinic Signature:</li>
    </ul>
    <p class="supplied">Purchased through <span class="site">www.bernardwhitlow.com.au</span></p>
    <div class="clinic-mark"><span class="dot"></span><span class="name">Bernard Whitlow</span></div>
  </section>
</body>
</html>
```